Poster advertising a workshop on digital analytics

Poster to market a workshop I'm presenting. I work in digital analytics and my workshop will talk about how analytics used to be done and what's changed. People will be able to go to heaps of different workshops so I need a poster to make mine stand out.

Attachments:
* Poster copy to use.
* Two headshots you can use, select the one that best fits your design.
* Company logo
* Example of the poster wall from last years' conference, to give you an idea.

Poster specs:
A2 size at a portrait orientation
420mm x 594mm
5mm Bleed with Crop Marks
CMYK

Target Market(s)

Marketers

Industry/Entity Type

Marketing

Font styles to use
Serif
Sans Serif

Colors

Designer to choose colors to be used in the design.

Requirements
Must have
• Eye catching

```html
<!DOCTYPE html>
<html lang="en">
<head>
<meta charset="utf-8">
<title>Driftline Analytics – Workshop Poster</title>
<link rel="stylesheet" href="https://fonts.googleapis.com/css2?family=Didact+Gothic&family=Montserrat:wght@500;600&display=swap">
<style>
  :root {
    --stage: #5b5b5b;
    --ink: #0b0b0b;
    --white: #ffffff;
    --sky: #2ba3e3;
    --blue: #1f8fd0;
    --deep-blue: #0f5f9a;
    --night: #050b12;
  }
  * { margin: 0; padding: 0; box-sizing: border-box; }
  html, body {
    width: 1049px; height: 1200px; overflow: hidden;
    background: var(--stage);
  }
  .poster {
    position: absolute; left: 174px; top: 54px;
    width: 702px; height: 996px;
    background: var(--ink);
    overflow: hidden;
    color: var(--white);
    box-shadow: 0 6px 24px rgba(0,0,0,.45);
  }
  .poster__shapes { position: absolute; inset: 0; width: 100%; height: 100%; }
  .brand {
    position: absolute; right: 30px; top: 26px;
    font-family: "Didact Gothic", sans-serif;
    font-size: 36px; line-height: 1;
    color: var(--sky);
    white-space: nowrap;
  }
  .headline {
    position: absolute;
    font-family: "Didact Gothic", sans-serif;
    font-weight: 400; line-height: 1; white-space: nowrap;
  }
  .headline--first { left: 8px; top: 160px; font-size: 59px; }
  .headline--second { left: 286px; top: 244px; font-size: 80px; }
  .intro {
    position: absolute; left: 276px; top: 336px; width: 410px;
    font-family: "Montserrat", sans-serif; font-weight: 600;
    font-size: 17px; line-height: 30px; letter-spacing: -0.2px;
    text-align: justify;
  }
  .section-title {
    position: absolute;
    font-family: "Didact Gothic", sans-serif; font-weight: 400;
    line-height: 1; white-space: nowrap;
    transform: scaleY(1.3); transform-origin: left top;
  }
  .section-title--presenter { left: 4px; top: 630px; font-size: 33px; }
  .section-title--cover { left: 282px; top: 630px; font-size: 45px; }
  .bio {
    position: absolute; left: 18px; top: 680px; width: 234px;
    font-family: "Montserrat", sans-serif; font-weight: 500;
    font-size: 16px; line-height: 29px;
  }
  .topics {
    position: absolute; left: 264px; top: 712px; width: 430px;
    list-style: none;
    font-family: "Montserrat", sans-serif; font-weight: 500;
    font-size: 18.5px; line-height: 34px;
  }
  .topics li { position: relative; padding-left: 26px; }
  .topics li::before {
    content: ""; position: absolute; left: 2px; top: 11px;
    width: 13px; height: 13px; border-radius: 50%; background: var(--white);
  }
</style>
</head>
<body>
<main class="poster">
  <svg class="poster__shapes" viewBox="0 0 468 665" preserveAspectRatio="none">
    <defs>
      <linearGradient id="tech-tone" x1="0" y1="0" x2="1" y2="1">
        <stop offset="0" stop-color="#8fd3f5"/>
        <stop offset=".45" stop-color="#2ba3e3"/>
        <stop offset="1" stop-color="#0b3f6e"/>
      </linearGradient>
      <linearGradient id="body-tone" x1="0" y1="0" x2="1" y2="0">
        <stop offset="0" stop-color="#2ba3e3"/>
        <stop offset=".7" stop-color="#1a6aa8"/>
        <stop offset="1" stop-color="#050b12"/>
      </linearGradient>
      <linearGradient id="column-tone" x1="0" y1="0" x2="0" y2="1">
        <stop offset="0" stop-color="#2ba3e3"/>
        <stop offset="1" stop-color="#1a7fc2"/>
      </linearGradient>
      <linearGradient id="streak-tone" x1="0" y1="0" x2="1" y2="0">
        <stop offset="0" stop-color="#2ba3e3"/>
        <stop offset="1" stop-color="#050b12"/>
      </linearGradient>
      <linearGradient id="photo-tone" x1="0" y1="0" x2="0" y2="1">
        <stop offset="0" stop-color="#9a9a9a"/>
        <stop offset="1" stop-color="#3a3a3a"/>
      </linearGradient>
    </defs>
    <path class="tech-backdrop" role="img" aria-label="Blue digital data backdrop" d="M0 0 H225 L210 76 H174 V164 H0 Z" fill="url(#tech-tone)"/>
    <polygon class="body-panel" points="174,76 284,76 468,214 468,404 174,404" fill="url(#body-tone)"/>
    <polygon class="light-streak" points="174,76 284,76 235,200 174,200" fill="#6cc4ee" opacity=".5"/>
    <rect class="presenter-column" x="0" y="404" width="174" height="236" fill="url(#column-tone)"/>
    <rect class="presenter-band" x="0" y="414" width="174" height="36" fill="#0f5f9a"/>
    <rect class="cover-band" x="177" y="414" width="291" height="50" fill="#2ba3e3"/>
    <polygon class="cover-streak" points="177,464 290,464 325,640 177,640" fill="url(#streak-tone)"/>
    <rect class="footer-strip" x="0" y="640" width="468" height="25" fill="#0b0b0b"/>
    <rect class="presenter-photo" role="img" aria-label="Black and white headshot of the presenter" x="0" y="164" width="174" height="240" fill="url(#photo-tone)"/>
  </svg>

  <div class="brand">Driftline Analytics</div>

  <h1 class="headline headline--first">Analytics has changed,</h1>
  <h1 class="headline headline--second">have you?</h1>

  <p class="intro">Analytics isn't the afterthought it once was, but has rapidly become the driver of digital businesses. Tools have got more sophisticated and practices have improved the reliability and breadth of what's recorded. Is your business still stuck doing it the 1990s way, and what can you do about it? Marcus walks through the evolution of digital analytics, how to do things properly today and where things are headed.</p>

  <h2 class="section-title section-title--presenter">THE PRESENTER</h2>
  <p class="bio">Marcus Hale has been doing Internet stuff for 25 years and got into digital analytics while trying to understand what people were doing on web sites and why. He loves joining the dots between different sets of data in order to tell a story.</p>

  <h2 class="section-title section-title--cover">WE WILL COVER</h2>
  <ul class="topics">
    <li>Your grandmother's Digital Analytics</li>
    <li>Tag management to move fast</li>
    <li>Data assurance to prevent breaking things</li>
    <li>Tool improvements and changes</li>
    <li>How to get to the new world of modern digital analytics</li>
  </ul>
</main>
</body>
</html>
```